Webdesign für Holding-Firma
Zielgruppe
Die velunto Holding ist eine Holding-Firma mit drei Tochtergesellschaften: velunto trusted advisors, velutno Real estate und Velunto GmbH. Wir haben Beteiligungen in IT-Unternehmen, Real Estate sowie kleine und mittlere Startups.
Aufgabenstellung
Das Design sollte nicht zu bunt sein und eher schlicht und futuristisch gestaltet sein. Gerne können die Farben aus den verschiedenen Logos verarbeitet werden.

```html
<!DOCTYPE html>
<html lang="de">
<head>
<meta charset="utf-8">
<title>velutno Real estate</title>
<link rel="stylesheet" href="https://fonts.googleapis.com/css2?family=Roboto+Condensed:wght@700&family=Roboto:wght@300;400;500&family=Open+Sans:wght@700&display=swap">
<style>
:root{
  --green:#4fc17d;
  --badge:#27b45f;
  --yellow:#f0f20c;
  --ink:#2b2b2b;
  --text:#3a3a3a;
  --muted:#555;
  --footer:#f0f0f0;
  --line:#dcdcdc;
  --hero-a:#4c7c55;
  --hero-b:#2f5d3c;
  --mark:#8ccf3c;
}
*{margin:0;padding:0;box-sizing:border-box}
html,body{width:948px;height:1200px;overflow:hidden;background:#fff}
body{position:relative;font-family:'Roboto',sans-serif;color:var(--text);font-weight:300}
.abs{position:absolute}
.site-header{left:0;top:0;width:948px;height:76px;background:#fff}
.brand{left:130px;top:14px;display:flex;align-items:center;gap:10px}
.brand-square{width:34px;height:34px;background:var(--mark)}
.brand-name{font-family:'Roboto',sans-serif;font-weight:500;font-size:24px;line-height:24px;color:var(--ink);letter-spacing:.5px}
.brand-sub{font-weight:400;font-size:10px;color:var(--ink);display:block;margin-top:2px;letter-spacing:.3px}
.lang{left:772px;top:32px;font-size:11px;font-weight:400;letter-spacing:1.2px;color:var(--ink)}
.hero{left:0;top:76px;width:948px;height:166px;background:linear-gradient(180deg,var(--hero-a),var(--hero-b))}
.hero-title{left:0;top:136px;width:948px;text-align:center;font-family:'Open Sans',sans-serif;font-weight:700;font-size:27px;line-height:32px;color:var(--yellow);padding-left:14px}
.hero-rule{left:458px;top:170px;width:33px;height:2px;background:var(--yellow)}
.h2{font-family:'Roboto Condensed',sans-serif;font-weight:700;font-size:21px;line-height:24px;color:var(--green);letter-spacing:.2px}
.copy{font-size:10.5px;line-height:18px}
.services{list-style:none;font-size:10.5px;line-height:18px;font-weight:400;color:var(--ink)}
.services li{display:flex;align-items:center;gap:6px}
.services svg{width:14px;height:12px}
.year{font-size:10.5px;font-weight:500;color:var(--ink)}
.badge{width:43px;height:18px;background:var(--badge);color:#fff;font-size:10.5px;font-weight:400;line-height:18px;padding-left:9px}
.photo{top:720px;width:212px;height:132px}
.p1{left:127px;background:linear-gradient(160deg,#6f7b57,#d9dadc 55%,#3c3328)}
.p2{left:368px;background:linear-gradient(160deg,#2f3a55,#4b5878 50%,#1e2335)}
.p3{left:608px;background:linear-gradient(120deg,#d7dadd,#8e9196 50%,#e2e4e6)}
.partners{left:127px;top:944px;width:693px;display:flex;justify-content:space-between;align-items:center}
.partner{font-family:'Roboto',sans-serif;font-weight:500;font-size:20px;color:var(--ink);width:152px}
.site-footer{left:0;top:1018px;width:948px;height:139px;background:var(--footer);border-top:1px solid var(--line);border-bottom:1px solid var(--line)}
.footer-mark{left:127px;top:1041px;width:56px;height:56px;background:#dcdcdc}
.footer-col{top:1044px;font-size:10.6px;line-height:15.4px;font-weight:400;letter-spacing:.6px;color:var(--ink)}
.footer-col strong{font-weight:500}
.copyright{left:0;top:1171px;width:948px;text-align:center;font-size:9.5px;font-weight:300;color:var(--ink)}
</style>
</head>
<body>
<header class="abs site-header">
  <div class="abs brand">
    <span class="brand-square"></span>
    <span class="brand-name">VELUNTO<span class="brand-sub">REAL ESTATE</span></span>
  </div>
  <div class="abs lang">DE&nbsp;&nbsp;|&nbsp;&nbsp;EN</div>
</header>

<section class="abs hero" role="img" aria-label="Flache Illustration einer grünen Stadtsilhouette mit Häusern und Laternen"></section>
<h1 class="abs hero-title">VELUTNO REAL ESTATE</h1>
<div class="abs hero-rule"></div>

<h2 class="abs h2" style="left:127px;top:268px">WER SIND WIR?</h2>
<p class="abs copy" style="left:128px;top:301px;width:330px">Wir sind ein Unternehmen velunto group und entwickeln, bauen, investieren und verwalten Wohn- und Gewerbeimmobilien.</p>

<h2 class="abs h2" style="left:511px;top:268px">WAS TUN WIR?</h2>
<ul class="abs services" style="left:511px;top:300px">
  <li><svg viewBox="0 0 14 12"><path d="M1 6.5l4 4 8-9" fill="none" stroke="#444" stroke-width="2.6"/></svg>Projektinvestment</li>
  <li><svg viewBox="0 0 14 12"><path d="M1 6.5l4 4 8-9" fill="none" stroke="#444" stroke-width="2.6"/></svg>Projektentwicklung</li>
  <li><svg viewBox="0 0 14 12"><path d="M1 6.5l4 4 8-9" fill="none" stroke="#444" stroke-width="2.6"/></svg>Projektplanung und Realisierung</li>
  <li><svg viewBox="0 0 14 12"><path d="M1 6.5l4 4 8-9" fill="none" stroke="#444" stroke-width="2.6"/></svg>Asset-Management</li>
  <li><svg viewBox="0 0 14 12"><path d="M1 6.5l4 4 8-9" fill="none" stroke="#444" stroke-width="2.6"/></svg>Immobiliendienstleistungen</li>
</ul>

<h2 class="abs h2" style="left:127px;top:435px">PROJEKT AUENWIESEN, TALBACH</h2>
<p class="abs copy" style="left:128px;top:466px">Errichtung eines Campus als neuer Firmensitz der nimbuswatt GmbH und den anderen Unternehmen der velunto group</p>

<h2 class="abs h2" style="left:127px;top:514px">NEWS</h2>
<div class="abs year" style="left:127px;top:545px">2019</div>
<div class="abs badge" style="left:127px;top:566px">Juni</div>
<div class="abs badge" style="left:500px;top:567px">Juli</div>
<p class="abs copy" style="left:127px;top:592px;width:320px">Vorstellung des Projektes im Gemeinderat der Stadt Talbach</p>
<p class="abs copy" style="left:500px;top:592px;width:330px">Gemeinderat der Stadt Talbach befürwortet mit deutlicher Mehrheit unser vorgeschlagenes Immobilienprojekt auf den Auenwiesen</p>

<h2 class="abs h2" style="left:127px;top:651px">AKTUELLER PROJEKTSTATUS</h2>
<p class="abs copy" style="left:127px;top:680px">Aktuell laufen die Planungsarbeiten in Zusammenarbeit mit der Stadt Talbach auf Hochtouren</p>

<div class="abs photo p1" role="img" aria-label="Foto: weißer Bauhelm auf Bauplänen im Freien"></div>
<div class="abs photo p2" role="img" aria-label="Foto: nächtliche Stadt überblendet mit Arbeit am Laptop"></div>
<div class="abs photo p3" role="img" aria-label="Foto: Bauleiter mit Helm und Klemmbrett vor einem Hochhaus"></div>

<h2 class="abs h2" style="left:127px;top:908px">PLANER &amp; PARTNER</h2>
<div class="abs partners">
  <span class="partner">nimbuswatt</span>
  <span class="partner">Fernblick</span>
  <span class="partner">kenntnisreich</span>
  <span class="partner">QUADRANTO AG</span>
</div>

<footer>
  <div class="abs site-footer"></div>
  <div class="abs footer-mark"></div>
  <div class="abs footer-col" style="left:374px">
    <strong>velunto Holding GmbH</strong><br>
    Lindenweg 4<br>
    77810 Talbach<br>
    contact@velunto.de<br>
    +49 (7000) 412 380 12
  </div>
  <div class="abs footer-col" style="left:647px">
    <strong>Rechtliches:</strong><br>
    GF: Jonas Reller und Lina Reller<br>
    HRB 412380<br>
    Steuer-Nr.: 25071/90214
  </div>
  <div class="abs copyright">Copyright 2020. All rights reserved.</div>
</footer>
</body>
</html>
```